Granite Ridge Holdings

I have a real estate investment business.

** I need editable vector files of the final design.

Industry/Entity Type

Real Estate

Contact Information for Business Card

I would like the card to be clear and direct with the company name and contact info. I would prefer not to have a design that is too busy (i.e., with excessive detail) in the business card.

Font styles to use
Sans Serif

Requirements
Must have
• My card must have the following information listed below:
• Company name: Grainite Ridge Holdings LLC
• My name: Daniel Vorsley
• Phone number: (555) 218-9067
• Email address: dtvorsley@mailbox-example.net
• Keywords: “Real Estate Investments”
Nice to have
• I would like to have a design that resembles the characteristics/uses of obsidian stone which resembles something related to strength and resilience. Perhaps something with sharp, sleek color transitions as well.

```html
<!DOCTYPE html>
<html lang="en">
<head>
<meta charset="UTF-8">
<title>Granite Ridge Holdings – Business Card</title>
<link href="https://fonts.googleapis.com/css2?family=Roboto+Condensed:wght@700&family=Montserrat:wght@400;500&family=Arimo:wght@400&display=swap" rel="stylesheet">
<style>
  :root {
    --page-bg: #ffffff;
    --card-bg: #fdfdfd;
    --ink-strong: #111111;
    --ink-body: #4a4a4a;
    --ink-soft: #555555;
    --rule: #222222;
    --stone-dark: #2a2522;
    --stone-mid: #5e5651;
    --stone-light: #8c847e;
  }
  html, body {
    margin: 0;
    padding: 0;
    width: 1200px;
    height: 1200px;
    overflow: hidden;
    background: var(--page-bg);
  }
  .business-card {
    position: absolute;
    left: 120px;
    top: 325px;
    width: 960px;
    height: 549px;
    background: var(--card-bg);
    box-shadow: 0 0 0 1px #eeeeee;
    overflow: hidden;
  }
  .stone-accent {
    position: absolute;
  }
  .stone-accent--top-left {
    left: 0;
    top: 0;
    width: 236px;
    height: 153px;
    background: linear-gradient(135deg, var(--stone-dark), var(--stone-mid) 60%, var(--stone-light));
  }
  .stone-accent--bottom-right {
    right: 0;
    bottom: 0;
    width: 273px;
    height: 160px;
    background: linear-gradient(135deg, var(--stone-light), var(--stone-mid) 45%, var(--stone-dark));
  }
  .company-name {
    position: absolute;
    left: 49px;
    top: 258px;
    margin: 0;
    font-family: "Roboto Condensed", "Arial Narrow", sans-serif;
    font-weight: 700;
    font-size: 35px;
    line-height: 1;
    letter-spacing: -0.6px;
    color: var(--ink-strong);
    white-space: nowrap;
  }
  .divider {
    position: absolute;
    left: 479px;
    top: 191px;
    width: 2px;
    height: 167px;
    background: var(--rule);
  }
  .person {
    position: absolute;
    left: 534px;
    top: 184px;
    font-family: "Montserrat", Arial, sans-serif;
    color: var(--ink-body);
  }
  .person-name {
    margin: 0;
    font-weight: 500;
    font-size: 32px;
    line-height: 40px;
    letter-spacing: 0.5px;
  }
  .person-title {
    margin: 0;
    font-weight: 400;
    font-size: 25px;
    line-height: 32px;
    letter-spacing: 0.5px;
  }
  .contact-list {
    position: absolute;
    left: 537px;
    top: 304px;
    margin: 0;
    padding: 0;
    list-style: none;
    font-family: "Montserrat", Arial, sans-serif;
    font-size: 19px;
    color: var(--ink-body);
  }
  .contact-item {
    display: flex;
    align-items: center;
    height: 34px;
    white-space: nowrap;
  }
  .contact-icon {
    width: 24px;
    height: 20px;
    margin-right: 17px;
    flex: none;
  }
  .tagline {
    position: absolute;
    left: 0;
    width: 958px;
    top: 472px;
    margin: 0;
    text-align: center;
    font-family: "Arimo", Arial, sans-serif;
    font-size: 29px;
    line-height: 1;
    color: var(--ink-soft);
  }
</style>
</head>
<body>
  <div class="business-card">
    <div class="stone-accent stone-accent--top-left" role="img" aria-label="Watercolour obsidian stone illustration in black and grey"></div>

    <h1 class="company-name">Grainite Ridge Holdings LLC</h1>

    <div class="divider"></div>

    <div class="person">
      <p class="person-name">Daniel Vorsley</p>
      <p class="person-title">Manager</p>
    </div>

    <ul class="contact-list">
      <li class="contact-item">
        <svg class="contact-icon" viewBox="0 0 24 20" aria-hidden="true">
          <path d="M9 2 C6 4 4 9 5 14 C5.5 17 7 19 8 19 L10 16 L8 13 C7.6 11 8 8 9.5 6 L12 6 L12 3 Z" fill="var(--ink-body)"/>
        </svg>
        <span>(555) 218-9067</span>
      </li>
      <li class="contact-item">
        <svg class="contact-icon" viewBox="0 0 24 20" aria-hidden="true">
          <rect x="1" y="4" width="20" height="13" fill="var(--ink-body)"/>
          <path d="M1 4 L11 12 L21 4" fill="none" stroke="#ffffff" stroke-width="1.6"/>
          <path d="M1 17 L8 10 M21 17 L14 10" stroke="#ffffff" stroke-width="1.2"/>
        </svg>
        <span>dtvorsley@mailbox-example.net</span>
      </li>
    </ul>

    <p class="tagline">Real Estate Investments</p>

    <div class="stone-accent stone-accent--bottom-right" role="img" aria-label="Watercolour obsidian stone illustration in black and grey"></div>
  </div>
</body>
</html>
```